Paws and Meadows is a dog walking service that offers home boarding and pet taxi

I am looking for a eye catching A5 leaflet/flyer design for my dog walking business Paws and Meadows.

The flyer must have my company logo on it (jpeg), a picture of my van (jpeg) and a picture of dogs playing (jpegs 1-5).

The fonts must be easy to read. I am not set on any colour scheme but do like the idea of having a natural background. IE. Green grass and blue sky or some forest setting with green trees. If you don't like this idea or its hard to work with don't worry I am open minded so be creative and do what you thinks best.

I'll provide quick feedback to designs that i like and so we can work together.

The flyers must contain the following:

60 minute group and individual walks
GPS Tracked Walks
Home Boarding
Pet Taxi
Puppy/Pet visits

Offer: 50% off first weeks dogs walks with this flyer.

As well as containing my contact info:

07915382046
www.paws-and-meadows.co.uk
paws-and-meadows@mailbrook.co.uk

Chatterbook, Chirpline and Snapgallery logos must be present as well.

Thanks and Good luck!

Target Market(s)

ANYONE WHO NEEDS THEIR DOG WALKED OR LOOKED AFTER WHEN THEY ARE ON HOLIDAY

Industry/Entity Type

Business

Contact Information for Business Card

THE BUSINESS CARD MUST DISPLAY THE LOGO THAT HAS BEEN UPLOADED IN A FILE. IT MUST LOOK SHARP AND PROFESSIONAL. CONTAIN ALL CONTACT INFO AND HAVE SERVICES OFFERED. SEE PROJECT DESCRIPTION FOR FLYER.

Font styles to use
Serif
Sans Serif

Requirements
Must have
• SEE PROJECT DESCRIPTION
Nice to have
• IT WOULD BE NICE TO HAVE PHOTOS OF MY VAN AND DOGS PLAYING. I HAVE UPLOADED SOME PICS OF VAN TO BE USED AND THERE ARE PICS OF DOGS PLAYING THAT COULD BE USED.

```html
<!DOCTYPE html>
<html lang="en">
<head>
<meta charset="utf-8">
<title>Paws and Meadows – Dog Walking Service</title>
<link rel="stylesheet" href="https://fonts.googleapis.com/css2?family=Ubuntu:wght@400;500;700&display=swap">
<style>
  :root {
    --lime: #a6d15b;
    --lime-band: #b2d86c;
    --lime-deep: #8fc043;
    --ink: #222222;
    --contact-green: #2f7c21;
    --accent-orange: #e0683a;
    --paper: #ffffff;
    --grass-1: #7fae3f;
    --grass-2: #b9d88a;
    --coat: #c98a3e;
  }
  * { box-sizing: border-box; margin: 0; padding: 0; }
  html, body { width: 845px; height: 1200px; overflow: hidden; background: var(--paper); }
  body { font-family: "Ubuntu", sans-serif; color: var(--ink); }
  .flyer { position: relative; width: 845px; height: 1200px; overflow: hidden; background: var(--paper); }

  .backdrop { position: absolute; inset: 0; }

  .brand { position: absolute; top: 38px; left: 0; width: 100%; text-align: center; }
  .brand-name { font-weight: 500; font-size: 68px; letter-spacing: 3px; color: var(--ink); text-transform: uppercase; line-height: 1; }
  .brand-tagline { display: flex; align-items: center; justify-content: center; gap: 12px; margin-top: 14px; font-size: 21px; letter-spacing: 5px; text-transform: uppercase; color: var(--ink); }
  .brand-tagline::before, .brand-tagline::after { content: ""; width: 70px; height: 4px; background: linear-gradient(90deg, transparent, var(--contact-green)); border-radius: 2px; }
  .brand-tagline::after { background: linear-gradient(90deg, var(--contact-green), transparent); }

  .services { position: absolute; top: 196px; left: 0; list-style: none; }
  .services li { position: absolute; left: 186px; white-space: nowrap; font-size: 29px; line-height: 1; }
  .services li::before { content: ""; position: absolute; top: 3px; width: 24px; height: 24px; border-radius: 50%; background: var(--ink); }
  .services li:nth-child(odd)::before { left: -122px; }
  .services li:nth-child(even)::before { left: -70px; }
  .services li:nth-child(1) { top: 0; }
  .services li:nth-child(2) { top: 61px; }
  .services li:nth-child(3) { top: 122px; }
  .services li:nth-child(4) { top: 182px; }
  .services li:nth-child(5) { top: 243px; }

  .gallery { position: absolute; inset: 0; pointer-events: none; }

  .social-title { position: absolute; top: 627px; left: 48px; font-size: 29px; font-weight: 700; }
  .social-list { position: absolute; top: 690px; left: 45px; list-style: none; }
  .social-list li { display: flex; align-items: center; height: 48px; margin-bottom: 36px; font-size: 19px; white-space: nowrap; }
  .social-list li::before { content: ""; width: 48px; height: 48px; background: var(--lime-deep); margin-right: 28px; flex: none; }

  .offer { position: absolute; top: 963px; left: 0; width: 100%; height: 48px; background: var(--lime-band); display: flex; align-items: center; justify-content: center; font-size: 26px; font-weight: 500; }

  .footer-brand { position: absolute; top: 1062px; left: 34px; width: 150px; display: flex; flex-direction: column; align-items: center; gap: 8px; }
  .footer-brand .mark { width: 46px; height: 46px; border-radius: 50%; background: var(--lime-deep); }
  .footer-brand .name { font-size: 16px; font-weight: 500; text-align: center; line-height: 1.15; }

  .contact { position: absolute; top: 1076px; left: 190px; list-style: none; font-size: 16px; line-height: 24px; white-space: nowrap; }
  .contact .phone, .contact .email { color: var(--contact-green); }
  .contact .web { color: var(--accent-orange); }

  .van-photo { position: absolute; top: 1055px; left: 470px; width: 158px; height: 82px; border: 3px solid var(--lime-deep); border-radius: 6px; background: linear-gradient(180deg, #8fb6d8 0%, #dfe6ea 45%, #9bbf5c 46%, #6f9a3c 100%); }
  .van-note { position: absolute; top: 1076px; left: 645px; width: 170px; font-size: 18px; line-height: 24px; color: var(--accent-orange); }
</style>
</head>
<body>
<main class="flyer">
  <svg class="backdrop" width="845" height="1200" viewBox="0 0 845 1200" aria-hidden="true">
    <path d="M0,144 L845,144 L845,262 Q620,585 0,555 Z" fill="var(--lime)"/>
  </svg>

  <header class="brand">
    <h1 class="brand-name">Paws and Meadows</h1>
    <p class="brand-tagline">Dog Walking Service</p>
  </header>

  <ul class="services">
    <li>60 minute group and individual walks</li>
    <li>GPS Tracked Walks</li>
    <li>Home Boarding</li>
    <li>Pet Taxi</li>
    <li>Puppy/Pet visits</li>
  </ul>

  <svg class="gallery" width="845" height="1200" viewBox="0 0 845 1200">
    <defs>
      <linearGradient id="grass" x1="0" y1="0" x2="0" y2="1">
        <stop offset="0" stop-color="var(--grass-2)"/>
        <stop offset="1" stop-color="var(--grass-1)"/>
      </linearGradient>
      <linearGradient id="lawnCoat" x1="0" y1="0" x2="0" y2="1">
        <stop offset="0" stop-color="#8cb35a"/>
        <stop offset="0.55" stop-color="var(--coat)"/>
        <stop offset="1" stop-color="#6f9a3c"/>
      </linearGradient>
    </defs>
    <g stroke="var(--lime-deep)" stroke-width="5">
      <ellipse role="img" aria-label="Photo of a black dog running on grass" cx="512" cy="520" rx="52" ry="64" fill="url(#grass)"/>
      <ellipse role="img" aria-label="Photo of small dogs playing on grass" cx="655" cy="515" rx="45" ry="62" fill="url(#grass)"/>
      <ellipse role="img" aria-label="Photo of a dog walking on grass" cx="428" cy="622" rx="44" ry="58" fill="url(#grass)"/>
      <ellipse role="img" aria-label="Photo of a dog in a park" cx="745" cy="625" rx="45" ry="60" fill="url(#grass)"/>
      <path role="img" aria-label="Photo of a greyhound in a park" d="M622,672 C695,672 775,745 775,815 C775,890 705,908 622,890 C540,908 470,890 470,815 C470,745 550,672 622,672 Z" fill="url(#lawnCoat)"/>
    </g>
  </svg>

  <h2 class="social-title">Follow us on:</h2>
  <ul class="social-list">
    <li>Chirpline.com/paws-and-meadows</li>
    <li>Chatterbook.com/paws-and-meadows</li>
    <li>Snapgallery.com/paws-and-meadows</li>
  </ul>

  <p class="offer">Offer: 50% off first weeks dogs walks with this flyer.</p>

  <div class="footer-brand">
    <span class="mark"></span>
    <span class="name">Paws and Meadows</span>
  </div>

  <ul class="contact">
    <li class="phone">07915382046</li>
    <li class="web">www.paws-and-meadows.co.uk</li>
    <li class="email">paws-and-meadows@mailbrook.co.uk</li>
  </ul>

  <div class="van-photo" role="img" aria-label="Photo of the company van parked on a grass verge"></div>
  <p class="van-note">check our fully insured caged van!</p>
</main>
</body>
</html>
```